Tarnby Group letterhead

Hi,

I need a letterhead template created for our business. This should be done in word format and A4 size. The images need to not move in the template ie when I am adding writing in etc. and should flow on when I get to a second page.

I have attached our logo templates below.

Other details to include on the letterhead somewhere are:

0438 915 267
Max@Tarnbyelectrical.example.au
PO Box 817 Marrowvale NSW 2190
ABN: 57 318 962 407

Thanks!

```html
<!DOCTYPE html>
<html lang="en">
<head>
<meta charset="utf-8">
<title>Tarnby Group Letterhead</title>
<link href="https://fonts.googleapis.com/css2?family=Montserrat:wght@600;700&family=Arimo:wght@400&display=swap" rel="stylesheet">
<style>
  :root {
    --backdrop: #e6e6e8;
    --paper: #ffffff;
    --ink: #2b2b2b;
    --ink-soft: #444444;
    --accent: #f25406;
    --band-dark: #1c1c1c;
    --rule: #555555;
  }
  * { box-sizing: border-box; margin: 0; padding: 0; }
  html, body {
    width: 1200px; height: 960px; overflow: hidden;
    background: var(--backdrop);
  }
  .letterhead {
    position: absolute; left: 282px; top: 30px;
    width: 636px; height: 900px;
    background: var(--paper);
    box-shadow: 0 4px 18px rgba(0,0,0,0.12);
    font-family: "Arimo", Arial, sans-serif;
    color: var(--ink-soft);
  }
  .brand {
    position: absolute; left: 58px; top: 70px;
    display: flex; align-items: center; gap: 10px;
  }
  .brand-dot {
    width: 30px; height: 30px; border-radius: 50%;
    background: var(--accent);
  }
  .brand-name {
    font-family: "Montserrat", Arial, sans-serif;
    font-weight: 700; font-size: 22px; letter-spacing: 1px;
    text-transform: uppercase; color: var(--ink);
  }
  .contact {
    position: absolute; left: 410px; top: 52px;
    padding-left: 14px; border-left: 1px solid var(--rule);
    font-size: 9.5px; line-height: 1.45; color: var(--ink-soft);
  }
  .contact-line { display: flex; align-items: center; gap: 4px; }
  .contact-line svg { width: 8px; height: 8px; fill: var(--accent); }
  .contact-label { color: var(--accent); }
  .letter-body {
    position: absolute; left: 96px; top: 300px; width: 440px;
  }
  .salutation {
    font-family: "Montserrat", Arial, sans-serif;
    font-weight: 700; font-size: 14px; color: var(--ink);
    margin-bottom: 14px;
  }
  .paragraph {
    font-size: 9.8px; line-height: 1.32; color: var(--ink-soft);
    margin-bottom: 14px;
  }
  .closing {
    font-family: "Montserrat", Arial, sans-serif;
    font-weight: 600; font-size: 9px; color: var(--ink);
    margin-top: 10px;
  }
  .signature {
    width: 130px; height: 34px; margin-top: 14px; margin-left: 60px;
    background: linear-gradient(90deg, #f1f1f1, #e4e4e4);
    border-radius: 3px;
  }
  .footer-bands {
    position: absolute; left: 0; bottom: 0; width: 636px; height: 40px;
  }
</style>
</head>
<body>
  <main class="letterhead">
    <header>
      <div class="brand">
        <span class="brand-dot"></span>
        <span class="brand-name">Tarnby Group</span>
      </div>
      <address class="contact" style="font-style:normal">
        <div>PO Box 817</div>
        <div>Marrowvale NSW 2190</div>
        <div class="contact-line">
          <svg viewBox="0 0 10 10"><path d="M2 1h2l1 2.5-1.3 1a5 5 0 0 0 2.8 2.8l1-1.3L10 7v2a1 1 0 0 1-1 1A9 9 0 0 1 0 1a1 1 0 0 1 1-1z"/></svg>
          <span>0438 915 267</span>
        </div>
        <div class="contact-line">
          <svg viewBox="0 0 10 10"><path d="M0 2h10v6H0zM0 2l5 3.5L10 2v1L5 6.5 0 3z" fill-rule="evenodd"/></svg>
          <span>Max@Tarnbyelectrical.example.au</span>
        </div>
        <div><span class="contact-label">ABN:</span> 57 318 962 407</div>
      </address>
    </header>

    <section class="letter-body">
      <p class="salutation">Dear Mr. Dalton,</p>
      <p class="paragraph">Lorem ipsum dolor sit amet, consectetuer adipiscing elit, sed diam nonummy nibh euismod tincidunt ut laoreet dolore magna aliquam erat volutpat. Ut wisi enim ad minim veniam, quis nostrud exerci tation ullamcorper suscipit lobortis nisl ut aliquip ex ea commodo consequat. Duis autem vel eum iriure dolor in hendrerit in vulputate velit esse molestie consequat, vel illum dolore eu feugiat</p>
      <p class="paragraph">Rorem ipsum dolor sit amet, consectetuer adipiscing elit, sed diam nonummy nibh euismod tincidunt ut laoreet dolore magna aliquam erat volutpat. Ut wisi enim ad minim veniam, quis nostrud exerci tation ullamcorper suscipit lobortis nisl ut aliquip ex ea commodo consequat. Duis autem vel eum iriure dolor in hendrerit in vulputate velit esse molest</p>
      <p class="paragraph">Dorem ipsum dolor sit amet, consectetuer adipiscing elit, sed diam nonummy nibh euismod tincidunt ut laoreet dolore magna aliquam erat volutpat. Ut wisi enim ad minim veniam, quis nostrud exerci tation ullamcorper suscipit lobortis nisl ut aliquip ex ea commodo consequat. Duis autem vel eum iriure dolor in hendrerit in suscipit lobortis nisl ut aliquip ex ea commodo consequat. Duis autem vel eum iriure dolor in hendrerit in vulputate velit esse molestie consequat, vel illum</p>
      <p class="paragraph">Sorem ipsum dolor sit amet, consectetuer adipiscing elit, sed diam nonummy nibh euismod tincidunt ut laoreet dolore magna aliquam erat volutpat. Ut wisi enim ad minim veniam, quis nostrud exerci tation ullamcorper suscipit lobortis nisl ut aliquip ex ea commodo consequat. Duis autem vel eum iriure dolor in</p>
      <p class="closing">Sincerely,</p>
      <div class="signature" role="img" aria-label="Handwritten signature"></div>
    </section>

    <svg class="footer-bands" viewBox="0 0 636 40" preserveAspectRatio="none" aria-hidden="true">
      <polygon points="0,22 370,22 352,40 0,40" fill="var(--band-dark)"/>
      <polygon points="395,0 636,0 636,40 357,40" fill="var(--accent)"/>
    </svg>
  </main>
</body>
</html>
```